Switch Kit - Banking Flyer

We want a design for an 8.5x11" flyer that matches the look of our website (www.morvalecommercebank.com). Outline is attached, but please feel free to include images/pictures/graphics that you think makes this easy to understand. The goal is to hand this flyer to a potential customer to get them to understand the information easily and quickly.

```html
<!DOCTYPE html>
<html lang="en">
<head>
<meta charset="utf-8">
<title>Morvale Commerce Bank – Switch Kit Flyer</title>
<link href="https://fonts.googleapis.com/css2?family=Roboto:wght@400;500;700&display=swap" rel="stylesheet">
<style>
  :root {
    --page-bg: #d6d6d6;
    --amber: #b4812f;
    --amber-light: #c99545;
    --navy: #2a3e5a;
    --navy-dark: #233550;
    --white: #ffffff;
    --photo-dark: #5a4128;
    --photo-mid: #9a7446;
  }
  * { box-sizing: border-box; margin: 0; padding: 0; }
  html, body {
    width: 1200px; height: 2365px; overflow: hidden;
    background: var(--page-bg);
    font-family: "Roboto", Arial, sans-serif;
    color: var(--white);
  }
  .flyer {
    position: absolute; left: 50px; top: 470px;
    width: 1100px; height: 1424px;
    box-shadow: -8px 8px 14px rgba(0,0,0,.35);
    overflow: hidden;
  }
  .hero {
    position: absolute; left: 0; top: 0; width: 1100px; height: 495px;
    background: var(--amber);
  }
  .hero-photo {
    position: absolute; right: 0; top: 0; width: 720px; height: 495px;
    background: linear-gradient(90deg, rgba(180,129,47,1) 0%, rgba(160,118,62,.85) 35%, var(--photo-mid) 60%, var(--photo-dark) 100%);
  }
  .brand {
    position: absolute; left: 45px; top: 58px;
    display: flex; align-items: center; gap: 14px;
    font-size: 40px; font-weight: 500; letter-spacing: 1px;
  }
  .brand-mark { width: 26px; height: 26px; background: var(--white); }
  .headline {
    position: absolute; left: 45px; top: 180px;
    font-size: 46px; font-weight: 500;
  }
  .headline strong { font-weight: 700; }
  .intro {
    position: absolute; left: 45px; width: 620px;
    font-size: 24px; line-height: 30px; font-weight: 400;
  }
  .intro.first { top: 265px; }
  .intro.second { top: 352px; }
  .divider { position: absolute; left: 0; top: 495px; width: 1100px; height: 4px; background: var(--white); }
  .steps {
    position: absolute; left: 0; top: 499px; width: 1100px; height: 811px;
    background: radial-gradient(circle at 70% 50%, var(--navy) 0%, var(--navy-dark) 100%);
  }
  .steps-lead {
    position: absolute; left: 45px; top: 38px;
    font-size: 24px; font-weight: 700;
  }
  .step-number {
    position: absolute; left: 43px;
    font-size: 60px; font-weight: 400; line-height: 1;
    color: transparent; -webkit-text-stroke: 2px var(--white);
  }
  .step-title {
    position: absolute; left: 133px; height: 48px;
    padding: 0 24px 0 14px; border-radius: 24px;
    background: var(--amber-light);
    font-size: 22px; font-weight: 500; line-height: 48px;
  }
  .step-text {
    position: absolute; left: 133px; width: 930px;
    font-size: 20.5px; line-height: 26px;
  }
  .flow-arrow { position: absolute; left: 72px; }
  .footer {
    position: absolute; left: 0; top: 1310px; width: 1100px; height: 114px;
    background: var(--amber);
  }
  .contact {
    position: absolute; display: flex; align-items: center; gap: 10px;
    font-weight: 500;
  }
  .contact.phone { left: 45px; top: 38px; font-size: 29px; }
  .contact.web { left: 330px; top: 42px; font-size: 22px; }
  .contact.place { left: 720px; top: 28px; font-size: 21px; line-height: 26px; }
</style>
</head>
<body>
<main class="flyer">
  <section class="hero">
    <div class="hero-photo" role="img" aria-label="Photograph of an old tractor seat and farm machinery inside a rustic wooden barn"></div>
    <div class="brand"><span class="brand-mark"></span>Morvale Commerce Bank</div>
    <h1 class="headline">Switching as easy as <strong>1-2-3!</strong></h1>
    <p class="intro first">One of the main reasons people don't switch banks is that it can be a hassle.</p>
    <p class="intro second">At Morvale Commerce Bank we make it easy. We value your time and with our efficient three step process, switching banks has never been easier.</p>
  </section>
  <div class="divider"></div>
  <section class="steps">
    <h2 class="steps-lead">We look forward to creating an exceptional experience for you at Morvale Commerce Bank.</h2>

    <div class="step-number" style="top:98px">01</div>
    <div class="step-title" style="top:100px">Open a Morvale Commerce Bank Account</div>
    <p class="step-text" style="top:168px">Stop by our branch and visit with our knowledgeable team to open your new account. We will be happy to assist you in choosing the right account for your banking needs.</p>
    <svg class="flow-arrow" style="top:162px" width="12" height="92" viewBox="0 0 12 92"><line x1="6" y1="0" x2="6" y2="82" stroke="#fff" stroke-width="1.5"/><path d="M1 80 L6 91 L11 80 Z" fill="#fff"/></svg>

    <div class="step-number" style="top:258px">02</div>
    <div class="step-title" style="top:261px">Stop using your old account and redirect your automatic payments and direct deposits</div>
    <p class="step-text" style="top:328px">It is important to remember to keep your old account open to ensure all your outstanding checks, deposits, and automatic withdrawals have cleared.</p>
    <p class="step-text" style="top:380px">We will provide you with a Payments Checklist to help you determine the companies you may need to notify of your account change so they can redirect any deposits or automatic withdrawals.</p>
    <p class="step-text" style="top:458px">Our Direct Deposit Change Notification and Notification of Automatic Withdrawal Change forms will easily allow companies to redirect your direct deposit(s) and automatic withdrawals to your new Morvale Commerce Bank account.</p>
    <svg class="flow-arrow" style="top:326px" width="12" height="290" viewBox="0 0 12 290"><line x1="6" y1="0" x2="6" y2="280" stroke="#fff" stroke-width="1.5"/><path d="M1 278 L6 289 L11 278 Z" fill="#fff"/></svg>

    <div class="step-number" style="top:622px">03</div>
    <div class="step-title" style="top:625px">Close your old account</div>
    <p class="step-text" style="top:692px">Now you are ready to switch. We will even provide an Account Closure Authorization form to close your old account. Any remaining account balance will be transferred to your Morvale Commerce Bank account.</p>
  </section>
  <footer class="footer">
    <div class="contact phone">
      <svg width="24" height="24" viewBox="0 0 24 24" fill="none" stroke="#fff" stroke-width="2"><path d="M5 3h4l2 5-2.5 1.5a11 11 0 0 0 6 6L16 13l5 2v4a2 2 0 0 1-2 2A16 16 0 0 1 3 5a2 2 0 0 1 2-2z"/><path d="M15 3a6 6 0 0 1 6 6M15 7a2 2 0 0 1 2 2"/></svg>
      (480) 555-0142
    </div>
    <div class="contact web">
      <svg width="22" height="22" viewBox="0 0 24 24" fill="none" stroke="#fff" stroke-width="1.6"><circle cx="12" cy="12" r="10"/><ellipse cx="12" cy="12" rx="4.5" ry="10"/><line x1="2" y1="12" x2="22" y2="12"/><path d="M4 6.5h16M4 17.5h16"/></svg>
      www.morvalecommercebank.com
    </div>
    <div class="contact place">
      <svg width="22" height="30" viewBox="0 0 22 30"><path d="M11 1a10 10 0 0 0-10 10c0 7 10 18 10 18s10-11 10-18A10 10 0 0 0 11 1z" fill="#fff"/><circle cx="11" cy="11" r="4" fill="#b4812f"/></svg>
      <span>2140 Cedar Ridge Avenue,<br>Suite 300 Fairhaven, AZ 85999</span>
    </div>
  </footer>
</main>
</body>
</html>
```